BUSINESS CARD DESIGN FOR CONSULTING BUSINESS

I need a business card design containing my logo and slogan for my new consulting business. The consulting business provides the following services: 1) human resource services assistance (payroll, expert advice, developing strategic and recruitment plans and blogs) for small businesses and 2) develops content for small business blogs and online magazines. I plan to expand the business, so I don't want to focus on the services but rather on my initials (HV) for name recognition and the name of the company, Dunmore Advisory Services.
My slogan is Practical, Thoughtful, Trusted Guidance.
I want a business card that is plain and not busy and contains a logo that reflects my work: consulting and writing. I would also like the business card to include the following contact information in this order: Helena Voss, Principal (lst line) Sr. Consultant (2nd line), 4737 Fenwick Lane, #273614, Ashgrove, CA 95712, (3rd line) hvossadvisoryservices@mailpost.example, (4th line), (916) 555-0172 (5th line), (my name, title, business address, email address, and phone number). My business's logo and name, Dunmore Advisory Services, should appear next to each other on the front of the card. The slogan should also be noted on the back of the card. Thanks!

Target Market(s)

Small businesses and governments.

Industry/Entity Type

Human Resources (HR) and Writing, but please focus on consulting services which can be both (HR and writing) or neither.

Logo Text

If possible, please create a abstract logo like the attachment. Or create a logo using my first and last initials (HV) and the word consulting like the Torvald Mesh (TM) example below.

Logo styles of interest
Abstract Logo
Wordmark Logo
Lettermark Logo
Font styles to use
Serif

Colors

Designer to choose colors to be used in the design.

Requirements
Must have
• Please feel free to create your own design as the attachment is just an example to show that I prefer a simple design with that format/layout if possible. The logo should be simple like a lettermark, word mark or abstract logo with the logo on the front and the slogan on the back. Please note my contact information in this order: my name with a title of Principal/Sr. Consultant, my address, email address and my phone number..
Nice to have
• Please see the attached sample design. A blue, or green or blue violet color card may look great. I am also good with simple black and white. Thanks!
Should not have
• Large, busy logo

```html
<!DOCTYPE html>
<html lang="en">
<head>
<meta charset="utf-8">
<title>Dunmore Advisory Services – Business Card</title>
<link rel="stylesheet" href="https://fonts.googleapis.com/css2?family=Cinzel:wght@400;600&family=Montserrat:wght@400&display=swap">
<style>
  :root {
    --backdrop: #6e6e6e;
    --card-white: #ffffff;
    --brand-blue: #1d56a3;
    --card-blue: #175193;
    --ink: #3d3d3d;
    --mark-grey: #9a9a9a;
    --on-blue: #ffffff;
  }
  * { margin: 0; padding: 0; box-sizing: border-box; }
  html, body { width: 900px; height: 1200px; overflow: hidden; }
  body { background: var(--backdrop); position: relative; font-family: "Montserrat", Arial, sans-serif; }

  .card {
    position: absolute; left: 80px; width: 742px; height: 440px;
    border-radius: 36px; box-shadow: 0 6px 8px rgba(0,0,0,0.45);
  }
  .card-front { top: 132px; background: var(--card-white); }
  .card-back { top: 638px; background: var(--card-blue); }

  .brand-name {
    font-family: "Cinzel", "Times New Roman", serif; font-weight: 600;
    line-height: 1; white-space: nowrap;
  }
  .brand-sub {
    display: flex; align-items: center; gap: 10px;
    font-family: "Cinzel", "Times New Roman", serif; font-weight: 600; line-height: 1;
  }
  .brand-sub::before, .brand-sub::after { content: ""; flex: 1; height: 2px; }

  /* Front: brand block */
  .brand-front { position: absolute; left: 34px; top: 168px; width: 300px; text-align: center; }
  .brand-front .brand-dot { width: 82px; height: 82px; border-radius: 50%; border: 8px solid var(--mark-grey); margin: 0 auto 16px; }
  .brand-front .brand-name { color: var(--brand-blue); font-size: 25px; }
  .brand-front .brand-sub { color: var(--mark-grey); font-size: 15px; margin-top: 4px; }
  .brand-front .brand-sub::before, .brand-front .brand-sub::after { background: var(--mark-grey); }

  .divider { position: absolute; left: 360px; top: 144px; width: 2px; height: 186px; background: var(--brand-blue); }

  /* Front: contact block */
  .contact { position: absolute; left: 384px; top: 138px; color: var(--ink); font-size: 16px; line-height: 20px; }
  .person-name {
    font-family: "Cinzel", "Times New Roman", serif; font-weight: 600;
    font-size: 28px; line-height: 34px; color: var(--brand-blue); margin-bottom: 2px;
  }
  .address { margin-top: 15px; }
  .reach { margin-top: 19px; }
  .reach-line { display: flex; align-items: center; gap: 9px; margin-left: 5px; height: 22px; font-size: 14.5px; white-space: nowrap; }
  .reach-line svg { width: 15px; height: 12px; fill: var(--brand-blue); flex: none; }

  /* Back */
  .brand-back { position: absolute; left: 145px; width: 452px; top: 114px; text-align: center; }
  .brand-back .brand-dot { width: 124px; height: 124px; border-radius: 50%; border: 12px solid var(--on-blue); margin: 0 auto 28px; }
  .brand-back .brand-name { color: var(--on-blue); font-size: 38px; }
  .brand-back .brand-sub { color: var(--on-blue); font-size: 22px; margin-top: 6px; }
  .brand-back .brand-sub::before, .brand-back .brand-sub::after { background: var(--on-blue); }
  .slogan { position: absolute; left: 0; right: 0; top: 388px; text-align: center; color: var(--on-blue); font-size: 19px; }
</style>
</head>
<body>
  <section class="card card-front">
    <div class="brand-front">
      <div class="brand-dot"></div>
      <p class="brand-name">Dunmore Advisory</p>
      <p class="brand-sub">Services</p>
    </div>
    <div class="divider"></div>
    <div class="contact">
      <h1 class="person-name">Helena Voss</h1>
      <p>Principal</p>
      <p>Sr. Consultant</p>
      <p class="address">4737 Fenwick Lane, #273614<br>Ashgrove, CA 95712</p>
      <div class="reach">
        <p class="reach-line">
          <svg viewBox="0 0 15 12" aria-hidden="true"><path d="M1 4 C1 1 14 1 14 4 L14 5 L10.5 5 L10.5 3.5 L4.5 3.5 L4.5 5 L1 5 Z M3 6 L12 6 L13.5 11 L1.5 11 Z"/></svg>
          (916) 555-0172
        </p>
        <p class="reach-line">
          <svg viewBox="0 0 15 12" aria-hidden="true"><path d="M1 2 L14 2 L14 3 L7.5 7 L1 3 Z M1 4.5 L7.5 8.5 L14 4.5 L14 11 L1 11 Z"/></svg>
          hvossadvisoryservices@mailpost.example
        </p>
      </div>
    </div>
  </section>

  <section class="card card-back">
    <div class="brand-back">
      <div class="brand-dot"></div>
      <p class="brand-name">Dunmore Advisory</p>
      <p class="brand-sub">Services</p>
    </div>
    <p class="slogan">Practical, Thoughtful, Trusted Guidance</p>
  </section>
</body>
</html>
```